Stroomwacht Powerpoint - presentation slides for energy management tool

We need a Powerpoint presentation lay-out which matches our logo from Stroomwacht.nl. 10 slides variations minimum, enough for a full professional presentation to potential clients.
Stroomwacht is a Dutch energymanagement tool for corporate real estate and housing agency. Our clients are Social houseing organisation, real estate owers, property managers and property developers.
Target Market(s)
real estate owners
Property manage
Font styles to use
Sans Serif
Colors
f78f20
0255a3
Requirements
Must have
- Stroomwacht logo colors and style
#F37122 orange
#00345D darkblue
Nice to have
- Professional look, background not white in every slide
Should not have
- wrong color orange and blue.

```html
<!DOCTYPE html>
<html lang="en">
<head>
<meta charset="utf-8">
<title>Stroomwacht Presentation Deck</title>
<link rel="stylesheet" href="https://fonts.googleapis.com/css2?family=Oswald:wght@500;600&family=Roboto:wght@300;400;700;900&display=swap">
<style>
:root{
  --orange:#F37122;
  --orange-2:#f78f20;
  --navy:#00345D;
  --blue:#0255a3;
  --ink:#1d2a38;
  --grey:#6b7480;
  --paper:#ffffff;
  --mist:#eef1f5;
  --line:#d9dee5;
}
*{box-sizing:border-box;margin:0;padding:0}
html,body{width:1200px;height:3240px;overflow:hidden}
body{background:var(--mist);font-family:Roboto,Arial,sans-serif;color:var(--ink);position:relative}

/* hero */
.hero{position:absolute;left:0;top:0;width:1200px;height:760px;background:linear-gradient(180deg,#c9d0d9 0%,#e4e8ee 45%,var(--mist) 100%)}
.hero-photo{position:absolute;left:0;top:0;width:1200px;height:330px;background:linear-gradient(180deg,rgba(70,84,104,.55),rgba(200,208,218,0))}
.hero-title{position:absolute;left:80px;top:290px;color:var(--navy)}
.hero-title b{display:block;font:900 66px/1 Roboto,sans-serif;letter-spacing:-1px}
.hero-title span{display:block;font:300 62px/1.1 Roboto,sans-serif}
.hero-slide{position:absolute;left:560px;top:170px;width:560px;height:315px;box-shadow:0 10px 30px rgba(0,30,60,.25);overflow:hidden}

/* deck grid */
.deck{position:absolute;left:90px;top:790px;display:grid;grid-template-columns:repeat(3,329px);gap:16px}
.deck-last{grid-column:1/4;display:flex;justify-content:center;gap:16px}
.s{position:relative;width:329px;height:185px;background:var(--paper);overflow:hidden;box-shadow:0 1px 4px rgba(0,30,60,.18)}
.s.dark{background:var(--navy)}

.mark{position:absolute;top:8px;right:10px;display:flex;align-items:center;gap:3px;font:700 6px Roboto,sans-serif;color:var(--navy)}
.mark i{width:6px;height:6px;background:var(--orange)}
.dark .mark,.mark.light{color:#fff}
.brand{display:flex;align-items:center;gap:5px;font:700 9px Roboto,sans-serif;color:#fff}
.brand i{width:9px;height:9px;background:var(--orange)}

.ph{position:absolute}
.ph-city{background:linear-gradient(135deg,#5a6d85,#2b3d55 60%,#c77a3c)}
.ph-office{background:linear-gradient(135deg,#c9b8a4,#7b8794 55%,#3c4a5c)}
.ph-build{background:linear-gradient(160deg,#b06a48,#7c5a4a 50%,#394656)}
.ph-tech{background:linear-gradient(135deg,#dfe5ec,#a8b5c4)}
.ph-hand{background:linear-gradient(135deg,#e8cfb5,#b99b86 60%,#6c7b8d)}

.cond{font-family:Oswald,Roboto,sans-serif;font-weight:500}
.t{position:absolute;font:900 12px/1.1 Roboto,sans-serif;color:var(--navy)}
.t.w{color:#fff}
.sub{position:absolute;font:700 6px/1.3 Roboto,sans-serif;color:var(--orange)}
.p{position:absolute;font:400 4.6px/1.55 Roboto,sans-serif;color:var(--grey)}
.p.w{color:#d6e2ee}
.box{position:absolute;border-radius:4px}
.dot{position:absolute;border-radius:50%}
.bar{position:absolute}
.row{display:flex}
svg{display:block}
table{border-collapse:collapse;font:400 4.6px Roboto,sans-serif}
</style>
</head>
<body>

<section class="hero">
  <div class="hero-photo" role="img" aria-label="Faded photo of a cheering crowd at an event"></div>
  <h1 class="hero-title"><b>Presentation</b><span>Deck</span></h1>
  <div class="hero-slide">
    <div class="ph ph-city" style="inset:0" role="img" aria-label="City skyline at dusk"></div>
    <div class="bar" style="inset:0;background:linear-gradient(90deg,rgba(0,52,93,.92) 40%,rgba(0,52,93,.3))"></div>
    <div class="brand" style="position:absolute;left:50px;top:50px;font-size:15px"><i style="width:14px;height:14px"></i>Stroomwacht</div>
    <div class="cond" style="position:absolute;left:50px;top:120px;font-size:30px;color:#fff">Presentation Title Goes Here</div>
    <div style="position:absolute;left:50px;top:170px;font:400 11px Roboto,sans-serif;color:#cfdceb">Subtitle or presenter name</div>
  </div>
</section>

<main class="deck">

  <!-- cover 1 -->
  <article class="s">
    <div class="ph ph-city" style="inset:0" role="img" aria-label="City skyline at dusk"></div>
    <div class="bar" style="inset:0;background:linear-gradient(90deg,rgba(0,52,93,.92) 40%,rgba(0,52,93,.35))"></div>
    <div class="brand" style="position:absolute;left:28px;top:28px"><i></i>Stroomwacht</div>
    <div class="cond" style="position:absolute;left:28px;top:72px;font-size:17px;color:#fff">Presentation Title Goes Here</div>
    <div class="p w" style="left:28px;top:100px">Subtitle or presenter name</div>
  </article>

  <!-- cover 2 -->
  <article class="s">
    <div class="ph ph-city" style="inset:0" role="img" aria-label="City street with office towers"></div>
    <div class="bar" style="inset:0;background:rgba(0,40,75,.78)"></div>
    <div class="brand" style="position:absolute;left:28px;top:28px"><i></i>Stroomwacht</div>
    <div class="cond" style="position:absolute;left:28px;top:72px;font-size:17px;color:#fff">Presentation Title Goes Here</div>
    <div class="bar" style="left:28px;top:100px;width:30px;height:2px;background:var(--orange)"></div>
  </article>

  <!-- cover 3 -->
  <article class="s">
    <div class="brand" style="position:absolute;left:28px;top:28px;color:var(--navy)"><i></i>Stroomwacht</div>
    <div class="cond" style="position:absolute;left:28px;top:72px;font-size:17px;color:var(--navy);width:150px">Presentation Title Goes Here</div>
    <div class="ph" style="right:0;top:0;width:140px;height:185px;background:linear-gradient(160deg,rgba(243,113,34,.25),rgba(2,85,163,.18))" role="img" aria-label="Line drawing of buildings in orange and blue"></div>
  </article>

  <!-- table of content -->
  <article class="s">
    <svg class="ph" style="left:0;top:0" width="150" height="185"><polygon points="0,0 150,0 100,185 0,185" fill="#00345D"/></svg>
    <div class="brand" style="position:absolute;left:16px;top:16px;font-size:6px"><i style="width:6px;height:6px"></i>Stroomwacht</div>
    <div class="t w" style="left:16px;top:120px">Table of Content</div>
    <div style="position:absolute;left:175px;top:42px;display:grid;gap:14px;font:400 5.5px Roboto,sans-serif;color:var(--ink)">
      <div class="row" style="gap:6px;align-items:center"><i style="width:5px;height:5px;background:var(--orange)"></i>Introduction</div>
      <div class="row" style="gap:6px;align-items:center"><i style="width:5px;height:5px;background:var(--orange)"></i>About the platform</div>
      <div class="row" style="gap:6px;align-items:center"><i style="width:5px;height:5px;background:var(--orange)"></i>Key benefits</div>
      <div class="row" style="gap:6px;align-items:center"><i style="width:5px;height:5px;background:var(--orange)"></i>Our clients</div>
      <div class="row" style="gap:6px;align-items:center"><i style="width:5px;height:5px;background:var(--orange)"></i>Next steps</div>
    </div>
  </article>

  <!-- welcome -->
  <article class="s">
    <div class="bar" style="left:0;top:0;width:36px;height:185px;background:var(--navy)"></div>
    <div style="position:absolute;left:6px;top:150px;transform:rotate(-90deg);transform-origin:left top;font:900 13px Roboto,sans-serif;color:#fff;letter-spacing:1px">WELCOME</div>
    <div class="ph ph-office" style="left:36px;top:0;width:170px;height:185px" role="img" aria-label="Two colleagues working on a laptop"></div>
    <div class="mark"><i></i>Stroomwacht</div>
    <div class="p" style="left:218px;top:60px;width:98px">Write a brief line that explains this idea to your audience. Add a short summary of your key point here.</div>
  </article>

  <!-- text page -->
  <article class="s">
    <div class="mark"><i></i>Stroomwacht</div>
    <div class="t" style="left:24px;top:24px">Text Page</div>
    <div class="sub" style="left:24px;top:42px">Subtitle goes here</div>
    <div class="p" style="left:24px;top:56px;width:280px">Write a brief line that explains this idea to your audience. Add a short summary of your key point here. Write a brief line that explains this idea to your audience. Add a short summary of your key point here.</div>
    <div class="p" style="left:24px;top:92px;width:280px">Write a brief line that explains this idea to your audience. Add a short summary of your key point here. Write a brief line that explains this idea to your audience.</div>
    <div class="p" style="left:24px;top:125px;width:280px">Add a short summary of your key point here. Write a brief line that explains this idea to your audience.</div>
  </article>

  <!-- two columns -->
  <article class="s">
    <div class="mark"><i></i>Stroomwacht</div>
    <div class="t" style="left:24px;top:24px">2 Column Text Page</div>
    <div class="sub" style="left:24px;top:44px">Subtitle</div>
    <div class="sub" style="left:172px;top:44px">Subtitle</div>
    <div class="p" style="left:24px;top:56px;width:132px">Write a brief line that explains this idea to your audience. Add a short summary of your key point here. Write a brief line that explains this idea to your audience.</div>
    <div class="p" style="left:172px;top:56px;width:132px">Add a short summary of your key point here. Write a brief line that explains this idea to your audience. Add a short summary of your key point here.</div>
  </article>

  <!-- mission -->
  <article class="s">
    <div class="mark"><i></i>Stroomwacht</div>
    <div class="bar" style="left:24px;top:50px;width:3px;height:50px;background:var(--orange)"></div>
    <div class="t" style="left:34px;top:52px;width:90px">Mission, Vision &amp; Goal</div>
    <div class="dot" style="left:150px;top:36px;width:16px;height:16px;background:var(--navy)"></div>
    <div class="sub" style="left:174px;top:36px">Mission</div>
    <div class="p" style="left:174px;top:44px;width:130px">Add a short summary of your key point here.</div>
    <div class="dot" style="left:150px;top:80px;width:16px;height:16px;background:var(--navy)"></div>
    <div class="sub" style="left:174px;top:80px">Vision</div>
    <div class="p" style="left:174px;top:88px;width:130px">Add a short summary of your key point here.</div>
    <div class="dot" style="left:150px;top:124px;width:16px;height:16px;background:var(--navy)"></div>
    <div class="sub" style="left:174px;top:124px">Goal</div>
    <div class="p" style="left:174px;top:132px;width:130px">Add a short summary of your key point here.</div>
  </article>

  <!-- three key points -->
  <article class="s">
    <div class="mark"><i></i>Stroomwacht</div>
    <div class="t" style="left:24px;top:24px">Three key points slide</div>
    <div class="box" style="left:24px;top:60px;width:88px;height:92px;background:var(--navy)"></div>
    <div class="box" style="left:120px;top:60px;width:88px;height:92px;background:var(--navy)"></div>
    <div class="box" style="left:216px;top:60px;width:88px;height:92px;background:var(--navy)"></div>
    <div class="p w" style="left:32px;top:80px;width:72px">Add a short summary of your key point here.</div>
    <div class="p w" style="left:128px;top:80px;width:72px">Add a short summary of your key point here.</div>
    <div class="p w" style="left:224px;top:80px;width:72px">Add a short summary of your key point here.</div>
  </article>

  <!-- benefits grid -->
  <article class="s">
    <div class="bar" style="left:0;top:18px;width:210px;height:30px;background:var(--navy)"></div>
    <div class="t w" style="left:20px;top:27px;font-size:10px">De voordelen van Stroomwacht</div>
    <div class="mark"><i></i>Stroomwacht</div>
    <div class="box" style="left:20px;top:70px;width:66px;height:80px;border:1px solid var(--line)"></div>
    <div class="box" style="left:94px;top:70px;width:66px;height:80px;border:1px solid var(--line)"></div>
    <div class="box" style="left:168px;top:70px;width:66px;height:80px;border:1px solid var(--line)"></div>
    <div class="box" style="left:242px;top:70px;width:66px;height:80px;border:1px solid var(--line)"></div>
    <div class="p" style="left:26px;top:80px;width:56px">Add a short summary of your key point.</div>
    <div class="p" style="left:100px;top:80px;width:56px">Add a short summary of your key point.</div>
    <div class="p" style="left:174px;top:80px;width:56px">Add a short summary of your key point.</div>
    <div class="p" style="left:248px;top:80px;width:56px">Add a short summary of your key point.</div>
  </article>

  <!-- nine key points -->
  <article class="s">
    <div class="mark"><i></i>Stroomwacht</div>
    <div class="t" style="left:24px;top:22px">9 key points slide</div>
    <div style="position:absolute;left:24px;top:50px;display:grid;grid-template-columns:repeat(3,94px);row-gap:14px">
      <div class="row" style="gap:4px"><i class="dot" style="position:static;width:10px;height:10px;background:var(--orange)"></i><span style="font:400 4.6px/1.5 Roboto,sans-serif;color:var(--grey);width:70px">Key point one text</span></div>
      <div class="row" style="gap:4px"><i class="dot" style="position:static;width:10px;height:10px;background:var(--orange)"></i><span style="font:400 4.6px/1.5 Roboto,sans-serif;color:var(--grey);width:70px">Key point two text</span></div>
      <div class="row" style="gap:4px"><i class="dot" style="position:static;width:10px;height:10px;background:var(--orange)"></i><span style="font:400 4.6px/1.5 Roboto,sans-serif;color:var(--grey);width:70px">Key point three text</span></div>
      <div class="row" style="gap:4px"><i class="dot" style="position:static;width:10px;height:10px;background:var(--orange)"></i><span style="font:400 4.6px/1.5 Roboto,sans-serif;color:var(--grey);width:70px">Key point four text</span></div>
      <div class="row" style="gap:4px"><i class="dot" style="position:static;width:10px;height:10px;background:var(--orange)"></i><span style="font:400 4.6px/1.5 Roboto,sans-serif;color:var(--grey);width:70px">Key point five text</span></div>
      <div class="row" style="gap:4px"><i class="dot" style="position:static;width:10px;height:10px;background:var(--orange)"></i><span style="font:400 4.6px/1.5 Roboto,sans-serif;color:var(--grey);width:70px">Key point six text</span></div>
      <div class="row" style="gap:4px"><i class="dot" style="position:static;width:10px;height:10px;background:var(--orange)"></i><span style="font:400 4.6px/1.5 Roboto,sans-serif;color:var(--grey);width:70px">Key point seven text</span></div>
      <div class="row" style="gap:4px"><i class="dot" style="position:static;width:10px;height:10px;background:var(--orange)"></i><span style="font:400 4.6px/1.5 Roboto,sans-serif;color:var(--grey);width:70px">Key point eight text</span></div>
      <div class="row" style="gap:4px"><i class="dot" style="position:static;width:10px;height:10px;background:var(--orange)"></i><span style="font:400 4.6px/1.5 Roboto,sans-serif;color:var(--grey);width:70px">Key point nine text</span></div>
    </div>
  </article>

  <!-- program -->
  <article class="s">
    <div class="bar" style="left:0;top:0;width:120px;height:185px;background:var(--navy)"></div>
    <div class="t w" style="left:16px;top:60px;width:95px;font-size:10px">Program content and deliverables slide</div>
    <div class="ph ph-office" style="left:140px;top:30px;width:170px;height:90px" role="img" aria-label="Modern office interior"></div>
    <div class="mark"><i></i>Stroomwacht</div>
    <div class="p" style="left:140px;top:130px;width:170px">Write a brief line that explains this idea to your audience.</div>
  </article>

  <!-- benefits photo -->
  <article class="s">
    <div class="ph ph-city" style="right:0;top:0;width:150px;height:185px" role="img" aria-label="Office building facade"></div>
    <div class="bar" style="left:0;top:60px;width:220px;height:40px;background:var(--navy)"></div>
    <div class="t w" style="left:18px;top:73px;font-size:10px">De voordelen van Stroomwacht</div>
    <div class="p" style="left:18px;top:115px;width:150px">Add a short summary of your key point here.</div>
  </article>

  <!-- building + title -->
  <article class="s">
    <div class="ph ph-build" style="left:0;top:0;width:120px;height:185px" role="img" aria-label="Brick apartment building"></div>
    <div class="mark"><i></i>Stroomwacht</div>
    <div class="t" style="left:136px;top:28px">Your Title Here</div>
    <div class="p" style="left:136px;top:48px;width:170px">Write a brief line that explains this idea to your audience. Add a short summary of your key point here.</div>
    <div class="box" style="left:136px;top:98px;width:80px;height:50px;background:var(--orange);border-radius:0"></div>
    <div class="p w" style="left:142px;top:106px;width:68px">Add a short summary of your key point.</div>
  </article>

  <!-- title + laptop -->
  <article class="s">
    <div class="mark"><i></i>Stroomwacht</div>
    <div class="t" style="left:24px;top:30px">Your Title Here</div>
    <div class="p" style="left:24px;top:50px;width:140px">Write a brief line that explains this idea to your audience. Add a short summary of your key point here. Write a brief line that explains this idea.</div>
    <div class="ph ph-tech" style="left:180px;top:55px;width:130px;height:100px" role="img" aria-label="Laptop on a desk"></div>
  </article>

  <!-- awesome two photos -->
  <article class="s">
    <div class="mark"><i></i>Stroomwacht</div>
    <div class="t" style="left:20px;top:30px;width:90px">Your awesome text here</div>
    <div class="p" style="left:20px;top:80px;width:90px">Add a short summary of your key point here.</div>
    <div class="ph ph-office" style="left:120px;top:30px;width:92px;height:80px" role="img" aria-label="Team meeting"></div>
    <div class="ph ph-tech" style="left:218px;top:30px;width:92px;height:80px" role="img" aria-label="People working at screens"></div>
    <div class="p" style="left:120px;top:118px;width:190px">Write a brief line that explains this idea to your audience.</div>
  </article>

  <!-- arrows -->
  <article class="s">
    <div class="mark"><i></i>Stroomwacht</div>
    <svg class="ph" style="left:104px;top:62px" width="121" height="60">
      <polygon points="0,30 24,6 24,18 58,18 58,42 24,42 24,54" fill="#00345D"/>
      <polygon points="121,30 97,6 97,18 63,18 63,42 97,42 97,54" fill="#F37122"/>
    </svg>
    <div class="sub" style="left:20px;top:60px">Option one</div>
    <div class="p" style="left:20px;top:70px;width:80px">Add a short summary of your key point here.</div>
    <div class="sub" style="left:232px;top:60px">Option two</div>
    <div class="p" style="left:232px;top:70px;width:80px">Add a short summary of your key point here.</div>
  </article>

  <!-- building half -->
  <article class="s">
    <div class="ph ph-build" style="left:0;top:0;width:160px;height:185px" role="img" aria-label="Tall residential building"></div>
    <div class="mark"><i></i>Stroomwacht</div>
    <div class="t" style="left:176px;top:50px;width:130px">Your Title Here</div>
    <div class="p" style="left:176px;top:70px;width:130px">Write a brief line that explains this idea to your audience.</div>
  </article>

  <!-- hand + list -->
  <article class="s">
    <div class="ph ph-hand" style="left:0;top:0;width:120px;height:185px" role="img" aria-label="Hand touching a digital screen"></div>
    <div class="bar" style="left:30px;top:20px;width:170px;height:20px;background:var(--orange)"></div>
    <div class="t w" style="left:40px;top:25px;font-size:9px">Your awesome text</div>
    <div class="mark"><i></i>Stroomwacht</div>
    <div class="p" style="left:136px;top:60px;width:175px">&#9632; Add a short summary of your key point here.<br>&#9632; Add a short summary of your key point here.<br>&#9632; Add a short summary of your key point here.<br>&#9632; Add a short summary of your key point here.</div>
  </article>

  <!-- monitor -->
  <article class="s">
    <div class="mark"><i></i>Stroomwacht</div>
    <div class="ph ph-tech" style="left:20px;top:40px;width:140px;height:100px" role="img" aria-label="Dashboard shown on a desktop monitor"></div>
    <div class="t" style="left:176px;top:44px">Your awesome text</div>
    <div class="p" style="left:176px;top:64px;width:135px">Write a brief line that explains this idea to your audience. Add a short summary of your key point here.</div>
  </article>

  <!-- dark awesome -->
  <article class="s dark">
    <div class="mark"><i></i>Stroomwacht</div>
    <div class="t w" style="left:20px;top:28px">Your awesome text</div>
    <div class="p w" style="left:20px;top:48px;width:120px">Write a brief line that explains this idea to your audience. Add a short summary of your key point here.</div>
    <div class="ph ph-tech" style="left:160px;top:50px;width:150px;height:100px" role="img" aria-label="Software screen on a laptop"></div>
  </article>

  <!-- mobiele app -->
  <article class="s">
    <div class="mark"><i></i>Stroomwacht</div>
    <div class="ph ph-tech" style="left:40px;top:25px;width:60px;height:140px;border-radius:8px;border:3px solid var(--navy)" role="img" aria-label="App screen on a smartphone"></div>
    <div class="t" style="left:130px;top:40px">Mobiele app</div>
    <div class="p" style="left:130px;top:60px;width:180px">Write a brief line that explains this idea to your audience. Add a short summary of your key point here.</div>
  </article>

  <!-- mobile app dark -->
  <article class="s dark">
    <div class="mark"><i></i>Stroomwacht</div>
    <div class="t w" style="left:20px;top:24px">Mobile app</div>
    <div class="ph ph-tech" style="left:120px;top:40px;width:56px;height:130px;border-radius:8px" role="img" aria-label="App screen on a smartphone"></div>
    <div class="bar" style="left:190px;top:60px;width:110px;height:24px;background:var(--orange)"></div>
    <div class="p w" style="left:196px;top:66px;width:100px">Add a short summary of your key point.</div>
    <div class="bar" style="left:190px;top:100px;width:110px;height:24px;background:var(--orange)"></div>
    <div class="p w" style="left:196px;top:106px;width:100px">Add a short summary of your key point.</div>
  </article>

  <!-- infographic donut -->
  <article class="s">
    <div class="mark"><i></i>Stroomwacht</div>
    <div class="t" style="left:20px;top:22px">Infographic</div>
    <svg class="ph" style="left:120px;top:50px" width="100" height="100" viewBox="0 0 100 100">
      <circle cx="50" cy="50" r="36" fill="none" stroke="#00345D" stroke-width="16" stroke-dasharray="54 172" transform="rotate(-90 50 50)"/>
      <circle cx="50" cy="50" r="36" fill="none" stroke="#F37122" stroke-width="16" stroke-dasharray="54 172" stroke-dashoffset="-56.5" transform="rotate(-90 50 50)"/>
      <circle cx="50" cy="50" r="36" fill="none" stroke="#0255a3" stroke-width="16" stroke-dasharray="54 172" stroke-dashoffset="-113" transform="rotate(-90 50 50)"/>
      <circle cx="50" cy="50" r="36" fill="none" stroke="#b9c3cf" stroke-width="16" stroke-dasharray="54 172" stroke-dashoffset="-169.5" transform="rotate(-90 50 50)"/>
    </svg>
    <div class="p" style="left:20px;top:60px;width:90px">Add a short summary of your key point.<br><br>Add a short summary of your key point.</div>
    <div class="p" style="left:232px;top:60px;width:85px">Add a short summary of your key point.<br><br>Add a short summary of your key point.</div>
  </article>

  <!-- four points -->
  <article class="s">
    <div class="mark"><i></i>Stroomwacht</div>
    <div class="t" style="left:20px;top:22px">Four Points</div>
    <svg class="ph" style="left:30px;top:50px" width="110" height="110" viewBox="0 0 110 110">
      <path d="M55 55V10A45 45 0 0 1 100 55Z" fill="#F37122"/>
      <path d="M55 55H100A45 45 0 0 1 55 100Z" fill="#00345D"/>
      <path d="M55 55V100A45 45 0 0 1 10 55Z" fill="#0255a3"/>
      <path d="M55 55H10A45 45 0 0 1 55 10Z" fill="#00345D"/>
      <line x1="88" y1="88" x2="106" y2="106" stroke="#00345D" stroke-width="6"/>
    </svg>
    <div class="p" style="left:170px;top:50px;width:140px">01 Add a short summary of your key point.<br><br>02 Add a short summary of your key point.<br><br>03 Add a short summary of your key point.<br><br>04 Add a short summary of your key point.</div>
  </article>

  <!-- infographic table -->
  <article class="s">
    <div class="mark"><i></i>Stroomwacht</div>
    <div class="t" style="left:20px;top:22px">Infographic</div>
    <table style="position:absolute;left:20px;top:50px;width:290px;color:var(--grey)">
      <tr style="background:var(--navy);color:#fff;height:14px"><th>Item</th><th style="background:var(--orange)">Basic</th><th>Plus</th><th>Pro</th></tr>
      <tr style="height:14px;text-align:center"><td>Meters</td><td>10</td><td>50</td><td>200</td></tr>
      <tr style="height:14px;text-align:center;background:var(--mist)"><td>Reports</td><td>1</td><td>5</td><td>20</td></tr>
      <tr style="height:14px;text-align:center"><td>Users</td><td>2</td><td>10</td><td>50</td></tr>
      <tr style="height:14px;text-align:center;background:var(--mist)"><td>Support</td><td>Email</td><td>Phone</td><td>Direct</td></tr>
    </table>
  </article>

  <!-- dark table -->
  <article class="s dark">
    <div class="mark"><i></i>Stroomwacht</div>
    <div class="t w" style="left:20px;top:22px">Your awesome text here</div>
    <table style="position:absolute;left:20px;top:50px;width:290px;background:#fff;color:var(--grey)">
      <tr style="background:var(--orange);color:#fff;height:14px"><th>Year</th><th>Q1</th><th>Q2</th><th>Q3</th><th>Q4</th></tr>
      <tr style="height:14px;text-align:center"><td>2019</td><td>12</td><td>18</td><td>20</td><td>24</td></tr>
      <tr style="height:14px;text-align:center"><td>2020</td><td>22</td><td>25</td><td>29</td><td>31</td></tr>
      <tr style="height:14px;text-align:center"><td>2021</td><td>30</td><td>34</td><td>38</td><td>42</td></tr>
    </table>
  </article>

  <!-- numbers -->
  <article class="s">
    <div class="mark"><i></i>Stroomwacht</div>
    <div class="t" style="left:0;width:329px;text-align:center;top:28px">Your awesome text</div>
    <div style="position:absolute;left:20px;top:80px;width:290px;display:flex;justify-content:space-around;font:900 16px Roboto,sans-serif;color:var(--navy)">
      <span>1M</span><span>2021</span><span>150+</span>
    </div>
    <div style="position:absolute;left:20px;top:104px;width:290px;display:flex;justify-content:space-around;font:400 4.6px Roboto,sans-serif;color:var(--grey)">
      <span>Readings per day</span><span>Founded in</span><span>Clients</span>
    </div>
  </article>

  <!-- line chart -->
  <article class="s">
    <div class="mark"><i></i>Stroomwacht</div>
    <div class="t" style="left:20px;top:22px">Your awesome text</div>
    <svg class="ph" style="left:20px;top:50px" width="290" height="110">
      <g stroke="#d9dee5" stroke-width=".6"><line x1="0" y1="20" x2="290" y2="20"/><line x1="0" y1="50" x2="290" y2="50"/><line x1="0" y1="80" x2="290" y2="80"/><line x1="0" y1="108" x2="290" y2="108"/></g>
      <polyline points="0,90 40,60 80,75 120,30 160,55 200,20 240,45 290,15" fill="none" stroke="#F37122" stroke-width="2"/>
      <polyline points="0,100 40,85 80,90 120,70 160,80 200,60 240,70 290,50" fill="none" stroke="#00345D" stroke-width="2"/>
    </svg>
  </article>

  <!-- rings -->
  <article class="s">
    <div class="mark"><i></i>Stroomwacht</div>
    <div class="t" style="left:0;width:329px;text-align:center;top:24px">Your awesome text</div>
    <svg class="ph" style="left:30px;top:60px" width="270" height="70" viewBox="0 0 270 70">
      <g fill="none" stroke-width="6">
        <circle cx="40" cy="35" r="28" stroke="#eef1f5"/><circle cx="40" cy="35" r="28" stroke="#F37122" stroke-dasharray="88 176" transform="rotate(-90 40 35)"/>
        <circle cx="135" cy="35" r="28" stroke="#eef1f5"/><circle cx="135" cy="35" r="28" stroke="#F37122" stroke-dasharray="132 176" transform="rotate(-90 135 35)"/>
        <circle cx="230" cy="35" r="28" stroke="#eef1f5"/><circle cx="230" cy="35" r="28" stroke="#F37122" stroke-dasharray="158 176" transform="rotate(-90 230 35)"/>
      </g>
      <g font-family="Roboto,sans-serif" font-weight="900" font-size="11" fill="#00345D" text-anchor="middle">
        <text x="40" y="39">50%</text><text x="135" y="39">75%</text><text x="230" y="39">90%</text>
      </g>
    </svg>
  </article>

  <!-- team -->
  <article class="s">
    <div class="mark"><i></i>Stroomwacht</div>
    <div class="t" style="left:20px;top:22px">Our Team</div>
    <div style="position:absolute;left:24px;top:50px;display:grid;grid-template-columns:repeat(3,96px);row-gap:12px;font:400 4.6px Roboto,sans-serif;color:var(--grey)">
      <div class="row" style="gap:5px;align-items:center"><i role="img" aria-label="Team member portrait" style="width:22px;height:22px;border-radius:50%;background:#c3cad3"></i><span><b style="color:var(--navy)">Lotte Vermeer</b><br>Director</span></div>
      <div class="row" style="gap:5px;align-items:center"><i role="img" aria-label="Team member portrait" style="width:22px;height:22px;border-radius:50%;background:#c3cad3"></i><span><b style="color:var(--navy)">Joris Bakker</b><br>Sales</span></div>
      <div class="row" style="gap:5px;align-items:center"><i role="img" aria-label="Team member portrait" style="width:22px;height:22px;border-radius:50%;background:#c3cad3"></i><span><b style="color:var(--navy)">Sanne de Wit</b><br>Support</span></div>
      <div class="row" style="gap:5px;align-items:center"><i role="img" aria-label="Team member portrait" style="width:22px;height:22px;border-radius:50%;background:#c3cad3"></i><span><b style="color:var(--navy)">Daan Kramer</b><br>Developer</span></div>
      <div class="row" style="gap:5px;align-items:center"><i role="img" aria-label="Team member portrait" style="width:22px;height:22px;border-radius:50%;background:#c3cad3"></i><span><b style="color:var(--navy)">Eva Smit</b><br>Analyst</span></div>
      <div class="row" style="gap:5px;align-items:center"><i role="img" aria-label="Team member portrait" style="width:22px;height:22px;border-radius:50%;background:#c3cad3"></i><span><b style="color:var(--navy)">Tim Visser</b><br>Advisor</span></div>
    </div>
  </article>

  <!-- clients -->
  <article class="s dark">
    <div class="t w" style="left:20px;top:60px;width:80px">Our Clients or Competitors</div>
    <div style="position:absolute;left:120px;top:30px;display:grid;grid-template-columns:repeat(3,58px);gap:8px">
      <i style="height:26px;background:rgba(255,255,255,.15)"></i><i style="height:26px;background:rgba(255,255,255,.15)"></i><i style="height:26px;background:rgba(255,255,255,.15)"></i>
      <i style="height:26px;background:rgba(255,255,255,.15)"></i><i style="height:26px;background:rgba(255,255,255,.15)"></i><i style="height:26px;background:rgba(255,255,255,.15)"></i>
      <i style="height:26px;background:rgba(255,255,255,.15)"></i><i style="height:26px;background:rgba(255,255,255,.15)"></i><i style="height:26px;background:rgba(255,255,255,.15)"></i>
      <i style="height:26px;background:rgba(255,255,255,.15)"></i><i style="height:26px;background:rgba(255,255,255,.15)"></i><i style="height:26px;background:rgba(255,255,255,.15)"></i>
    </div>
  </article>

  <!-- pictures and text -->
  <article class="s">
    <div class="bar" style="left:0;top:0;width:329px;height:40px;background:var(--navy)"></div>
    <div class="t w" style="left:20px;top:14px">Pictures and text</div>
    <div class="ph ph-office" style="left:20px;top:54px;width:90px;height:60px" role="img" aria-label="Office team"></div>
    <div class="ph ph-city" style="left:120px;top:54px;width:90px;height:60px" role="img" aria-label="City buildings"></div>
    <div class="ph ph-tech" style="left:220px;top:54px;width:90px;height:60px" role="img" aria-label="Energy dashboard on a screen"></div>
    <div class="p" style="left:20px;top:122px;width:90px">Add a short summary of your key point.</div>
    <div class="p" style="left:120px;top:122px;width:90px">Add a short summary of your key point.</div>
    <div class="p" style="left:220px;top:122px;width:90px">Add a short summary of your key point.</div>
  </article>

  <div class="deck-last">
    <!-- chapter -->
    <article class="s dark">
      <div class="ph" style="right:0;top:0;width:170px;height:185px;background:linear-gradient(160deg,rgba(2,85,163,.55),rgba(0,52,93,0))" role="img" aria-label="Faint line drawing of buildings"></div>
      <div class="t w" style="left:24px;top:110px">Chapter Number</div>
      <div class="p w" style="left:24px;top:126px">Chapter title here</div>
    </article>
    <!-- closing -->
    <article class="s" style="background:var(--mist)">
      <div class="box" style="left:94px;top:52px;width:140px;height:80px;background:#fff;box-shadow:0 3px 10px rgba(0,30,60,.15)"></div>
      <div style="position:absolute;left:94px;top:52px;width:140px;height:80px;display:flex;align-items:center;justify-content:center;gap:5px;font:700 13px Roboto,sans-serif;color:var(--navy)"><i style="width:11px;height:11px;background:var(--orange)"></i>Stroomwacht</div>
      <div class="p" style="left:0;width:329px;text-align:center;top:146px">Stroomwacht.nl</div>
    </article>
  </div>

</main>
</body>
</html>
```